Label

I need a label designed for a bottle of water. I like the lightning bolt and the blue. But I do not want it exactly like the Zinn-oop.

The label needs to be 9 inches by 2.5 inches.

Pebble Water: Sip the Pebble

```html
<!DOCTYPE html>
<html lang="en">
<head>
<meta charset="utf-8">
<title>Pebble Water – Bottle Label</title>
<link rel="stylesheet" href="https://fonts.googleapis.com/css2?family=Montserrat:wght@500;600;700&display=swap">
<style>
  :root {
    --sky-deep: #1f6fc4;
    --sky-mid: #5fa3e0;
    --sky-light: #b9dcf5;
    --haze: #f4f9fe;
    --brand-navy: #1c4a92;
    --label-white: #ffffff;
  }
  html, body {
    margin: 0;
    padding: 0;
    width: 1200px;
    height: 333px;
    overflow: hidden;
    background: var(--haze);
  }
  .label {
    position: relative;
    width: 1200px;
    height: 333px;
    overflow: hidden;
    font-family: "Montserrat", sans-serif;
  }
  .sky {
    position: absolute;
    inset: 0;
    background:
      radial-gradient(ellipse 420px 230px at 600px 150px, var(--haze) 0%, rgba(244,249,254,0.85) 35%, rgba(185,220,245,0) 100%),
      radial-gradient(ellipse 380px 160px at 250px 190px, rgba(255,255,255,0.7) 0%, rgba(255,255,255,0) 100%),
      radial-gradient(ellipse 320px 140px at 900px 130px, rgba(255,255,255,0.55) 0%, rgba(255,255,255,0) 100%),
      linear-gradient(180deg, var(--sky-mid) 0%, var(--sky-light) 45%, var(--sky-mid) 80%, var(--sky-deep) 100%);
  }
  .sky-rays {
    position: absolute;
    inset: 0;
  }
  .brand {
    position: absolute;
    left: 0;
    right: 0;
    top: 70px;
    text-align: center;
    color: var(--brand-navy);
  }
  .brand-name {
    margin: 0;
    font-size: 66px;
    font-weight: 600;
    letter-spacing: 0.02em;
    line-height: 1;
  }
  .brand-mark {
    display: inline-block;
    width: 18px;
    height: 18px;
    border-radius: 50%;
    background: var(--brand-navy);
    vertical-align: middle;
    margin-left: 14px;
    position: relative;
    top: -6px;
  }
  .tagline {
    margin: 18px 0 0;
    font-size: 20px;
    font-weight: 600;
    letter-spacing: 0.04em;
    color: var(--brand-navy);
  }
  .product-type {
    position: absolute;
    left: 0;
    right: 0;
    bottom: 12px;
    text-align: center;
    color: var(--label-white);
  }
  .product-type .qualifier {
    display: block;
    font-size: 13px;
    font-weight: 500;
    letter-spacing: 0.55em;
    margin-bottom: 4px;
    padding-left: 0.55em;
  }
  .product-type .kind {
    display: block;
    font-size: 19px;
    font-weight: 600;
    letter-spacing: 0.06em;
  }
</style>
</head>
<body>
  <main class="label">
    <div class="sky" role="img" aria-label="Soft blue sky with white clouds and bright light at the centre"></div>
    <svg class="sky-rays" width="1200" height="333" viewBox="0 0 1200 333" aria-hidden="true">
      <polygon points="0,260 520,120 560,140 0,333" fill="#ffffff" opacity="0.18"/>
      <polygon points="1200,40 700,150 720,170 1200,120" fill="#ffffff" opacity="0.2"/>
      <polygon points="1200,200 760,180 780,200 1200,290" fill="#ffffff" opacity="0.15"/>
      <polygon points="0,20 480,130 460,150 0,90" fill="#ffffff" opacity="0.15"/>
    </svg>

    <header class="brand">
      <h1 class="brand-name">Pebble Water<span class="brand-mark"></span></h1>
      <p class="tagline">Sip The Pebble</p>
    </header>

    <p class="product-type">
      <span class="qualifier">NATURAL</span>
      <span class="kind">SPRING WATER</span>
    </p>
  </main>
</body>
</html>
```